need a Flyer for Plush Toy company

Need a Flyer for Plush Toy company ,

I upload a file for TEXT

Target Market(s)

Toys wholesalers , Supermarket

Industry/Entity Type

Toy Store

Colors
000000
ec1f27
c4c4c4

Requirements
Must have
• I have up loaded 3 files
• 1. Logo Registered Brand
• 2. customer's design in drawing
• 3. our ready samples based on Design
Nice to have
• happy kids in Nature ,
• happy kids in Ski ,
• different color Kids ,
• Multi culture concept

```html
<!DOCTYPE html>
<html lang="en">
<head>
<meta charset="utf-8">
<title>Momo Lane – Plush Toy Flyer</title>
<link href="https://fonts.googleapis.com/css2?family=Open+Sans:wght@400;600;700;800&family=Dancing+Script:wght@700&display=swap" rel="stylesheet">
<style>
  :root {
    --red: #ec1f27;
    --black: #000000;
    --grey: #c4c4c4;
    --light: #eeeeee;
    --white: #ffffff;
    --ink: #222222;
  }
  * { margin: 0; padding: 0; box-sizing: border-box; }
  html, body { width: 800px; height: 1200px; overflow: hidden; background: var(--white); }
  body { font-family: "Open Sans", Arial, sans-serif; color: var(--ink); }
  .flyer { position: relative; width: 800px; height: 1200px; overflow: hidden; background: var(--white); }

  /* header */
  .header { position: absolute; left: 0; top: 0; width: 800px; height: 250px; }
  .brand-mark { position: absolute; left: 44px; top: 34px; display: flex; align-items: center; gap: 12px; }
  .brand-mark .dot { width: 40px; height: 40px; border-radius: 50%; background: var(--red); }
  .brand-mark .name { font-size: 30px; font-weight: 800; color: var(--ink); }
  .tagline-script { position: absolute; left: 40px; top: 150px; font-family: "Dancing Script", cursive; font-size: 32px; color: var(--red); }
  .company { position: absolute; left: 330px; top: 26px; width: 440px; text-align: center; }
  .company h1 { font-size: 54px; font-weight: 800; color: var(--ink); line-height: 1.1; }
  .company p { font-size: 21px; color: #333; line-height: 1.35; }
  .company .type { font-size: 24px; }
  .swoosh { position: absolute; left: 0; top: 170px; width: 800px; height: 110px; }

  /* product area */
  .products { position: absolute; left: 0; top: 250px; width: 800px; height: 250px;
    background: linear-gradient(180deg, #e61d25 0%, #d0141c 100%); }

  /* body text */
  .story { position: absolute; left: 0; top: 500px; width: 800px; height: 400px; background: var(--black);
    color: var(--white); padding: 38px 48px 0; font-size: 17.5px; line-height: 1.5; }
  .story p { margin-bottom: 20px; }
  .story .accent { color: var(--red); font-weight: 600; }
  .story .closing { padding-left: 24px; }

  /* footer */
  .footer { position: absolute; left: 0; top: 900px; width: 800px; height: 300px; background: var(--light); }
  .footer-art { position: absolute; left: 0; top: 0; width: 410px; height: 300px;
    background: linear-gradient(180deg, #f3f3f3 0%, #d9e6df 55%, #9fd3c3 100%); }
  .address { position: absolute; left: 20px; top: 218px; width: 340px; height: 66px; background: var(--red);
    color: var(--white); font-size: 20px; font-weight: 600; line-height: 1.3; padding: 6px 18px; }
  .contact { position: absolute; left: 430px; top: 28px; width: 350px; font-size: 14.5px; line-height: 1.5; color: #444; }
  .bank { margin-top: 16px; color: var(--red); font-weight: 700; font-size: 15.5px; line-height: 1.45; }
</style>
</head>
<body>
<div class="flyer">
  <header class="header">
    <div class="brand-mark"><span class="dot"></span><span class="name">Momo Lane</span></div>
    <div class="tagline-script">Have you been there?</div>
    <div class="company">
      <h1>Momo Lane</h1>
      <p class="type">Einzelunternehmen / Family Business</p>
      <p>International Trader for Toys</p>
      <p>Innovative Developer for Plush Toys</p>
    </div>
    <svg class="swoosh" viewBox="0 0 800 110" preserveAspectRatio="none">
      <path d="M0 70 C 220 10, 520 10, 800 40 L800 80 C 520 55, 230 60, 0 110 Z" fill="#c4c4c4"/>
      <path d="M0 85 C 230 35, 520 30, 800 55 L800 110 L0 110 Z" fill="#ec1f27"/>
    </svg>
  </header>

  <section class="products" role="img" aria-label="Row of colourful plush toy samples on a red background"></section>

  <section class="story">
    <p>We live and work in Talheim near to Cologne Germany. We speak German and English.</p>
    <p>The toys are made in China, we are small family business , but we are professional in Plush toys business , right now we have successfully&nbsp; launched Projects with a huge Japanese 100 Yen Chain Store.&nbsp; Here in Flyer we show a Sample project.</p>
    <p><span class="accent">100 Yen = 0.90 USD.</span> Our products can meet strictest Quality Control , but are with extremely Low Price to fit for&nbsp; Japanese Dollar Shop as well as his overseas Store around the world.</p>
    <p class="closing">Of course our products are fit for <span class="accent">Premium Store too.</span></p>
  </section>

  <footer class="footer">
    <div class="footer-art" role="img" aria-label="Illustration of plush toy characters sitting on a green sofa"></div>
    <div class="address">Lindenweg 8, 50999<br>Talheim Germany</div>
    <div class="contact">
      <div>hello@momolane.example</div>
      <div>Fon&nbsp;&nbsp; +49 (0) 2200- 555 0101</div>
      <div>Fax&nbsp;&nbsp; +49 (0) 2200- 555 0102</div>
      <div>Mobil:&nbsp; +49 (0) 150 5550 103</div>
      <div>Ust-IdNr /VAT No. DE000111222</div>
      <div class="bank">
        Bank information:<br>
        Kontoinhaber/Account Holder:<br>
        Lin Hart<br>
        IBAN:&nbsp; DE00 1234 5678 9012 3456 78<br>
        BIC : MOLADEXX000
      </div>
    </div>
  </footer>
</div>
</body>
</html>
```